Redesign one screen in a mobile app

I have an app called Toasts and Tallies (available on iOS and Android). This app allows wedding guests to bet on things that happen during a wedding they are attending (think: will the groom cry when the bride walks down the aisle...). The event is set up by someone called the "event leader", typically this is the bride or the groom.

Once event details, bets, and $ values of the bets are entered, the event leader publishes the event and gets to the event detail homescreen, where they can manage their event. The three main things they can do are:

1.) Share the event with other guests to join in the betting.
2.) Edit the event -- add, change, or delete bets.
3.) Add a co-organizer. If you are the bride or the groom, you want someone else managing the event on your wedding day.

I'd like to redesign this page, make it simpler, and *focus attention on sharing the event.* The biggest goal of this page is getting event leaders to share the event. We want them to invite as many wedding guests as possible.

To that end, I would like to also introducing "sharing tiers" to entice more sharing and I'd like this to be something event leaders can easily see once they hit the event homescreen. Tiers are as follows:
Share with 1 guest, unlock co-organizer feature.
Share with 5 guests, unlock physical placard with custom QR code.
Share with 10 guests, we split our proceeds with the bride and groom.
Share with 20 guests, you are entered into $250 monthly raffle.

Some additional requests:
+ Please do not use current fonts. We want new fonts that are cleaner.
+ Share options should stay the same (copy, share, QR code)
+ Need to keep "help" question mark on page as well.
+ Maintain colors generally. Red button color must be kept as is because it's used throughout app. Slight variations to other colors OK.
+ Navigation at bottom must remain.
+ Feel free to add moving elements as well, like gifs.
+ Final design delivered in Figma.
Updates

Submissions need to be app designs. Not webpages.

The current actions shown on the page need to remain - share event, edit event, add a Co-Organizer. But the goal of the design is to make the page simpler, not more complicated.

Sharing tiers can be a separate screen, linked from the event home screen. This information does not need to live on the same page!

Target Market(s)

25-40 year olds

Industry/Entity Type

Mobile Apps - Betting

Font styles to use
Sans Serif
Other font styles liked:
• I like poppins, but open to other options.

Requirements
Must have
• Fun design that focuses on sharing an event. Design delievered in Figma.

```html
<!DOCTYPE html>
<html lang="en">
<head>
<meta charset="utf-8">
<title>Toasts and Tallies – Event Details</title>
<link href="https://fonts.googleapis.com/css2?family=Roboto:wght@400;500;700&display=swap" rel="stylesheet">
<style>
:root{
  --red:#e06152;
  --red-text:#e0513f;
  --pink:#fdf0ef;
  --pill:#f9d9d7;
  --ink:#2b2b2b;
  --body:#333333;
  --field:#f1f1f1;
  --card:#f2f2f2;
  --nav:#2e2e2e;
  --icon-bg:#efefef;
  --muted:#9a9a9a;
}
*{margin:0;padding:0;box-sizing:border-box}
html,body{width:1200px;height:5270px;overflow:hidden;background:#fff}
body{font-family:'Roboto',sans-serif;color:var(--ink);position:relative}
.abs{position:absolute}
.panel{position:absolute;left:0;width:1200px;border-radius:120px 120px 0 0}
.panel.pink{background:var(--pink)}
.panel.white{background:#fff}
.heading{position:absolute;left:38px;font-size:48px;font-weight:700;letter-spacing:1px;line-height:56px;color:var(--ink)}
.underline{position:absolute;left:38px;width:125px;height:5px;background:var(--red);border-radius:3px}
.para{position:absolute;left:38px;width:1130px;font-size:38px;line-height:60px;color:var(--body);letter-spacing:.3px}
.event-photo{left:38px;top:485px;width:382px;height:379px;border-radius:24px;background:linear-gradient(160deg,#8aa4a8 0%,#5b6a5e 45%,#d8d6cf 75%,#3b3b3b 100%)}
.event-title{left:487px;top:488px;font-size:48px;font-weight:700;color:var(--red-text)}
.meta{font-size:38px;color:var(--ink);line-height:44px}
.bets-pill{left:482px;top:758px;width:262px;height:94px;border-radius:47px;background:var(--pill);display:flex;align-items:center;justify-content:center;gap:16px;font-size:38px}
.link-field{left:38px;top:1411px;width:1124px;height:137px;border-radius:68px;background:var(--field);display:flex;align-items:center;padding-left:44px;font-size:34px;color:var(--red-text)}
.btn{position:absolute;background:var(--red);color:#fff;font-weight:700;font-size:43px;display:flex;align-items:center;justify-content:center;gap:26px;border-radius:68px}
.share-btn{top:1594px;width:355px;height:137px}
.edit-btn{left:38px;top:2203px;width:1124px;height:127px;border-radius:64px}
.divider{left:38px;top:3019px;width:1124px;height:2px;background:#dedede}
.organizers-label{left:38px;top:3092px;font-size:43px;font-weight:500;color:var(--red-text)}
.organizer-card{left:38px;top:3194px;width:1124px;height:226px;border-radius:24px;background:var(--card)}
.avatar{left:72px;top:3216px;width:182px;height:182px;border-radius:50%;background:linear-gradient(160deg,#c9d6e0,#4f6f92)}
.organizer-name{left:302px;top:3282px;font-size:43px;color:var(--ink)}
.tier{position:absolute;left:38px;width:1124px;height:283px;background:#fff;border-radius:24px}
.tier-icon{position:absolute;left:34px;top:50px;width:182px;height:182px;border-radius:50%;background:var(--icon-bg);display:flex;align-items:center;justify-content:center}
.tier-title{position:absolute;left:255px;font-size:43px;font-weight:700;color:var(--red-text);letter-spacing:.5px}
.tier-desc{position:absolute;left:255px;width:680px;font-size:38px;line-height:54px;color:var(--body);letter-spacing:.3px}
.tier-arrow{position:absolute;left:1024px;top:114px;width:56px;height:56px;border-radius:50%;background:#f1eeee;display:flex;align-items:center;justify-content:center}
.bottom-nav{left:0;top:4987px;width:1200px;height:283px;background:var(--nav);border-radius:120px 120px 0 0}
.nav-item{position:absolute;top:5042px;width:200px;text-align:center;color:#fff;font-size:36px;font-weight:500}
.nav-circle{width:130px;height:130px;border-radius:50%;background:#fff;margin:0 auto 22px;display:flex;align-items:center;justify-content:center}
.nav-circle.active{background:var(--red)}
</style>
</head>
<body>

<!-- top bar -->
<svg class="abs" style="left:40px;top:124px" width="40" height="44" viewBox="0 0 40 44"><path d="M28 6 L12 22 L28 38" fill="none" stroke="#444" stroke-width="6" stroke-linecap="round" stroke-linejoin="round"/></svg>
<svg class="abs" style="left:1096px;top:116px" width="62" height="62" viewBox="0 0 62 62"><circle cx="31" cy="31" r="27" fill="none" stroke="#555" stroke-width="5"/><path d="M23 25a8 8 0 1 1 11 7c-2 1-3 2-3 5v2" fill="none" stroke="#555" stroke-width="5" stroke-linecap="round"/><circle cx="31" cy="46" r="3.5" fill="#555"/></svg>

<!-- event details -->
<section class="panel pink" style="top:235px;height:860px"></section>
<h1 class="heading" style="top:326px">EVENTS DETAILS</h1>
<div class="underline" style="top:401px"></div>
<div class="abs event-photo" role="img" aria-label="Photo of friends riding in an open-top jeep"></div>
<div class="abs event-title">Jeep Drive</div>
<svg class="abs" style="left:488px;top:596px" width="34" height="36" viewBox="0 0 34 36"><rect x="3" y="6" width="28" height="27" rx="3" fill="none" stroke="#e0513f" stroke-width="4"/><path d="M3 14h28M10 2v8M24 2v8" stroke="#e0513f" stroke-width="4"/><rect x="9" y="19" width="5" height="4" fill="#e0513f"/><rect x="17" y="19" width="5" height="4" fill="#e0513f"/><rect x="9" y="25" width="5" height="4" fill="#e0513f"/></svg>
<div class="abs meta" style="left:576px;top:592px">Feb 08</div>
<svg class="abs" style="left:832px;top:595px" width="40" height="40" viewBox="0 0 40 40"><circle cx="20" cy="20" r="16" fill="none" stroke="#e0513f" stroke-width="4"/><path d="M20 10v11l7 5" fill="none" stroke="#e0513f" stroke-width="4" stroke-linecap="round"/></svg>
<div class="abs meta" style="left:922px;top:592px">05:00pm</div>
<svg class="abs" style="left:490px;top:674px" width="30" height="40" viewBox="0 0 30 40"><path d="M15 2C7 2 2 8 2 15c0 10 13 23 13 23s13-13 13-23C28 8 23 2 15 2z" fill="#e0513f"/><circle cx="15" cy="15" r="5" fill="#fdf0ef"/></svg>
<div class="abs meta" style="left:576px;top:674px">Missouri</div>
<div class="abs bets-pill"><svg width="34" height="38" viewBox="0 0 34 38"><rect x="10" y="2" width="22" height="28" rx="3" fill="#e0513f"/><rect x="2" y="8" width="22" height="28" rx="3" fill="#e0513f" stroke="#f9d9d7" stroke-width="3"/></svg><span>3 Bets</span></div>

<!-- share -->
<section class="panel white" style="top:960px;height:900px"></section>
<h2 class="heading" style="top:1054px">SHARE YOUR EVENT</h2>
<div class="underline" style="top:1128px"></div>
<p class="para" style="top:1181px">Invite guests to join by sharing the event below. Each guest pays $2.99 to join, and if 101-guests join in the fun, we share the proceeds with the bride and groom!</p>
<div class="abs link-field">https://links.toastsandtallies.com/8saCZe81MhX6bsJWA</div>
<div class="btn share-btn" style="left:38px"><svg width="34" height="42" viewBox="0 0 34 42"><path d="M4 3h18l9 9v27H4z" fill="none" stroke="#fff" stroke-width="4" stroke-linejoin="round"/><path d="M11 22h13M11 30h13" stroke="#fff" stroke-width="4"/></svg>Copy</div>
<div class="btn share-btn" style="left:422px"><svg width="40" height="42" viewBox="0 0 40 42"><circle cx="31" cy="8" r="7" fill="#fff"/><circle cx="9" cy="21" r="7" fill="#fff"/><circle cx="31" cy="34" r="7" fill="#fff"/><path d="M31 8L9 21l22 13" fill="none" stroke="#fff" stroke-width="4"/></svg>Share</div>
<div class="btn share-btn" style="left:806px"><svg width="40" height="40" viewBox="0 0 40 40" fill="#fff"><path d="M2 2h16v16H2zM7 7v6h6V7zM22 2h16v16H22zM27 7v6h6V7zM2 22h16v16H2zM7 27v6h6v-6zM22 22h6v6h-6zM32 22h6v6h-6zM27 28h6v5h-6zM22 33h5v5h-5zM33 33h5v5h-5z" fill-rule="evenodd"/></svg>QR Code</div>

<!-- edit -->
<section class="panel pink" style="top:1814px;height:680px"></section>
<h2 class="heading" style="top:1918px">EDIT YOUR EVENT</h2>
<div class="underline" style="top:1992px"></div>
<p class="para" style="top:2036px">Change event details, add or delete bets, and change answer choices below.</p>
<div class="btn edit-btn"><svg width="38" height="38" viewBox="0 0 38 38"><path d="M4 34l2-9L26 5l7 7-20 20z" fill="#fff"/></svg>Edit Your Event</div>

<!-- co-organizer -->
<section class="panel white" style="top:2431px;height:1120px"></section>
<h2 class="heading" style="top:2523px">ASSIGN A CO-ORGANIZER</h2>
<div class="underline" style="top:2597px"></div>
<p class="para" style="top:2644px">If a bride or groom created this event, you'll want to assign a guest to be the co-organizer. This allows them to manage the event going forward, closing out all bets as they happen during the wedding weekend. Your co-organizer will get a notification to take over!</p>
<div class="abs divider"></div>
<div class="abs organizers-label">Event Organizers</div>
<svg class="abs" style="left:1116px;top:3095px" width="46" height="46" viewBox="0 0 46 46"><rect x="3" y="3" width="40" height="40" rx="7" fill="none" stroke="#e06152" stroke-width="4"/><path d="M23 12v22M12 23h22" stroke="#e06152" stroke-width="4"/></svg>
<div class="abs organizer-card"></div>
<div class="abs avatar" role="img" aria-label="Profile photo of the event organizer"></div>
<div class="abs organizer-name">Dan Mercer</div>

<!-- sharing tiers -->
<section class="panel pink" style="top:3499px;height:1600px"></section>
<h2 class="heading" style="top:3591px">SHARING TIERS</h2>
<div class="underline" style="top:3665px"></div>

<div class="tier" style="top:3727px">
  <div class="tier-icon"><svg width="86" height="86" viewBox="0 0 86 86" fill="none" stroke="#e06152" stroke-width="3"><circle cx="43" cy="20" r="12"/><circle cx="43" cy="20" r="5"/><circle cx="20" cy="52" r="7"/><circle cx="43" cy="52" r="7"/><circle cx="66" cy="52" r="7"/><path d="M8 78c0-10 24-10 24 0M31 78c0-10 24-10 24 0M54 78c0-10 24-10 24 0"/></svg></div>
  <div class="tier-title" style="top:58px">Share with 1 guest</div>
  <div class="tier-desc" style="top:122px">unlock co-organizer feature</div>
  <div class="tier-arrow"><svg width="40" height="20" viewBox="0 0 40 20"><path d="M2 10h32M26 3l8 7-8 7" fill="none" stroke="#333" stroke-width="3"/></svg></div>
</div>

<div class="tier" style="top:4034px">
  <div class="tier-icon"><svg width="80" height="80" viewBox="0 0 80 80" fill="none" stroke="#e06152" stroke-width="3"><path d="M4 16V4h12M64 4h12v12M76 64v12H64M16 76H4V64"/><rect x="16" y="16" width="18" height="18"/><rect x="46" y="16" width="18" height="18"/><rect x="16" y="46" width="18" height="18"/><path d="M46 46h8v8h-8zM58 58h6v6h-6zM46 60h6M58 46h6"/><path d="M4 40h72"/></svg></div>
  <div class="tier-title" style="top:56px">Share with 5 guests</div>
  <div class="tier-desc" style="top:118px">unlock physical placard with custom QR code</div>
  <div class="tier-arrow"><svg width="40" height="20" viewBox="0 0 40 20"><path d="M2 10h32M26 3l8 7-8 7" fill="none" stroke="#333" stroke-width="3"/></svg></div>
</div>

<div class="tier" style="top:4342px">
  <div class="tier-icon"><svg width="86" height="86" viewBox="0 0 86 86" fill="none" stroke="#e06152" stroke-width="3"><circle cx="28" cy="28" r="14"/><circle cx="58" cy="28" r="14"/><path d="M6 80V62c0-10 8-16 22-16s22 6 22 16M36 80V62c0-10 8-16 22-16s22 6 22 16v18"/><path d="M6 80h74"/></svg></div>
  <div class="tier-title" style="top:58px">Share with 10 guests</div>
  <div class="tier-desc" style="top:118px">we split our proceeds with the bride and groom</div>
  <div class="tier-arrow"><svg width="40" height="20" viewBox="0 0 40 20"><path d="M2 10h32M26 3l8 7-8 7" fill="none" stroke="#333" stroke-width="3"/></svg></div>
</div>

<div class="tier" style="top:4649px">
  <div class="tier-icon"><svg width="84" height="84" viewBox="0 0 84 84" fill="none" stroke="#e06152" stroke-width="3"><rect x="6" y="12" width="72" height="66" rx="6"/><path d="M6 28h72M24 4v14M60 4v14"/><rect x="16" y="38" width="10" height="8"/><rect x="32" y="38" width="10" height="8"/><rect x="48" y="38" width="10" height="8"/><rect x="62" y="38" width="8" height="8"/><rect x="16" y="54" width="10" height="8"/><rect x="32" y="54" width="10" height="8"/><rect x="48" y="54" width="10" height="8"/><rect x="62" y="54" width="8" height="8"/></svg></div>
  <div class="tier-title" style="top:82px">Share with 20 guests</div>
  <div class="tier-desc" style="top:146px;width:760px">you are entered into $250 monthly raffle</div>
  <div class="tier-arrow"><svg width="40" height="20" viewBox="0 0 40 20"><path d="M2 10h32M26 3l8 7-8 7" fill="none" stroke="#333" stroke-width="3"/></svg></div>
</div>

<!-- bottom navigation -->
<nav class="abs bottom-nav"></nav>
<div class="nav-item" style="left:44px"><div class="nav-circle active"><svg width="46" height="42" viewBox="0 0 46 42"><path d="M23 3L3 20h6v19h10V27h8v12h10V20h6z" fill="#fff"/></svg></div>Home</div>
<div class="nav-item" style="left:497px"><div class="nav-circle"><svg width="40" height="46" viewBox="0 0 40 46"><rect x="13" y="2" width="25" height="32" rx="3" fill="#e06152"/><rect x="3" y="10" width="25" height="32" rx="3" fill="#e06152" stroke="#fff" stroke-width="3"/></svg></div>My Bets</div>
<div class="nav-item" style="left:958px"><div class="nav-circle"><svg width="60" height="40" viewBox="0 0 60 40" fill="#e06152"><circle cx="30" cy="11" r="8"/><circle cx="12" cy="15" r="6"/><circle cx="48" cy="15" r="6"/><path d="M16 38c0-10 6-15 14-15s14 5 14 15zM2 36c0-7 4-11 10-11 3 0 5 1 6 2-2 3-3 6-3 9zM58 36c0-7-4-11-10-11-3 0-5 1-6 2 2 3 3 6 3 9z"/></svg></div>Leaders</div>

</body>
</html>
```